New Business Card Design Project

New business card design required for an electrical business in Australia. Offering quality electrical services including design and installation. Electrical services offered are domestic, commercial and industrial. Also meets all the air conditioning installation and maintenance needs.

Target Market(s)

The business is sleek, professional and caters primarily to wealthy clients and government contracts looking for exceptional, tailored service.

Industry/Entity Type

Electrical

Contact Information for Business Card

Damian Corlowe (Director)
0438 615 274
admin@vrtelectrical.com.au
www.vrtelectrical.com.au

Font styles to use
Sans Serif

Requirements
Must have
• The business card must show the license number - 64193 to comply with legislation.
Nice to have
• The logo colours and fonts could be incorporated into the design if the designer sees fit. We are open to new ideas and welcome creativity. The logo style guide is attached for reference if required.

```html
<!DOCTYPE html>
<html lang="en">
<head>
<meta charset="UTF-8">
<title>VRT Electrical – Business Card</title>
<link href="https://fonts.googleapis.com/css2?family=Poppins:wght@300;400;600;700&display=swap" rel="stylesheet">
<style>
  :root {
    --navy: #0f2a52;
    --navy-deep: #0d2750;
    --navy-soft: #1b3c70;
    --white: #ffffff;
    --grey: #8a8f98;
    --stage: #e9e9ec;
  }
  * { margin: 0; padding: 0; box-sizing: border-box; }
  html, body { width: 1200px; height: 780px; overflow: hidden; }
  body {
    background: var(--stage);
    font-family: "Poppins", sans-serif;
    display: flex;
    align-items: center;
    justify-content: center;
    gap: 40px;
  }
  .card {
    position: relative;
    width: 540px;
    height: 330px;
    border-radius: 22px;
    overflow: hidden;
    box-shadow: 0 6px 20px rgba(0,0,0,0.12);
  }
  .card-front { background: var(--white); }
  .card-back { background: var(--navy-deep); }

  .brand {
    position: absolute;
    display: flex;
    align-items: center;
    gap: 10px;
    font-family: "Poppins", sans-serif;
    font-weight: 600;
    letter-spacing: 2px;
    white-space: nowrap;
  }
  .brand-dot {
    width: 10px; height: 10px;
    border-radius: 50%;
  }
  .card-front .brand { right: 44px; top: 70px; font-size: 30px; color: var(--navy); }
  .card-front .brand-dot { background: var(--navy); }
  .card-back .brand { right: 44px; top: 150px; font-size: 30px; color: var(--navy-soft); }
  .card-back .brand-dot { background: var(--navy-soft); }

  .divider {
    position: absolute;
    left: 0; right: 0;
    top: 178px;
    height: 1.5px;
    background: var(--navy);
  }
  .side-tab {
    position: absolute;
    left: -18px; top: 120px;
    width: 36px; height: 36px;
    border-radius: 50%;
    background: var(--navy);
  }
  .person { position: absolute; left: 40px; top: 112px; }
  .person-name {
    font-weight: 700;
    font-size: 17px;
    letter-spacing: 0.5px;
    color: var(--navy);
    text-transform: uppercase;
  }
  .person-role {
    font-weight: 300;
    font-size: 14px;
    letter-spacing: 1px;
    color: var(--grey);
    text-transform: uppercase;
    line-height: 1.1;
  }
  .license {
    position: absolute;
    right: 0; top: 190px;
    background: var(--navy);
    color: var(--white);
    font-size: 12px;
    padding: 5px 22px 5px 18px;
    border-radius: 14px 0 0 14px;
  }
  .contacts {
    position: absolute;
    left: 36px; bottom: 30px;
    list-style: none;
  }
  .contact {
    display: flex;
    align-items: center;
    gap: 10px;
    font-size: 13px;
    color: var(--navy);
    line-height: 1;
    margin-top: 6px;
  }
  .contact-icon { width: 18px; height: 18px; flex: none; }
</style>
</head>
<body>
  <section class="card card-front">
    <div class="brand"><span class="brand-name">VRT ELECTRICAL</span><span class="brand-dot"></span></div>
    <div class="side-tab"></div>
    <div class="person">
      <p class="person-name">Damian Corlowe</p>
      <p class="person-role">Director</p>
    </div>
    <div class="divider"></div>
    <div class="license">license number - 64193</div>
    <ul class="contacts">
      <li class="contact">
        <svg class="contact-icon" viewBox="0 0 18 18"><circle cx="9" cy="9" r="9" fill="#0f2a52"/><path d="M6.2 4.6l1.4 1.9-.8 1.1c.5 1.1 1.4 2 2.5 2.5l1.1-.8 1.9 1.4-.6 1.5c-3.3-.2-6-2.9-6.2-6.2z" fill="#fff"/></svg>
        <span>0438 615 274</span>
      </li>
      <li class="contact">
        <svg class="contact-icon" viewBox="0 0 18 18"><circle cx="9" cy="9" r="9" fill="#0f2a52"/><rect x="4.5" y="6" width="9" height="6.2" rx="0.8" fill="#fff"/><path d="M4.8 6.3L9 9.4l4.2-3.1" stroke="#0f2a52" stroke-width="0.9" fill="none"/></svg>
        <span>admin@vrtelectrical.com.au</span>
      </li>
      <li class="contact">
        <svg class="contact-icon" viewBox="0 0 18 18"><circle cx="9" cy="9" r="9" fill="#0f2a52"/><g stroke="#fff" stroke-width="0.9" fill="none"><circle cx="9" cy="9" r="4.6"/><ellipse cx="9" cy="9" rx="2" ry="4.6"/><path d="M4.4 9h9.2"/></g></svg>
        <span>www.vrtelectrical.com.au</span>
      </li>
    </ul>
  </section>

  <section class="card card-back">
    <div class="brand"><span class="brand-name">VRT ELECTRICAL</span><span class="brand-dot"></span></div>
  </section>
</body>
</html>
```